入れる文字の内容は添付ファイルを参照してください。
タイトルのみ、添付の文字を使用してください。
配置等は特に決まりはありませんので、添付ファイルはあくまで参考でお願いします。
ターゲットは梅酒といえば若い女性をイメージしますが、今回は年配のおじさんをターゲットにしたいです。
そこからデザインイメージを膨らませて頂ければと思います

```html
<!DOCTYPE html>
<html lang="ja">
<head>
<meta charset="utf-8">
<title>琥珀梅・白露梅 梅酒</title>
<link href="https://fonts.googleapis.com/css2?family=Noto+Serif+JP:wght@500;700&display=swap" rel="stylesheet">
<style>
  :root {
    --paper: #ffffff;
    --ink: #1b1b1b;
    --title-ink: #2a1a0c;
    --label-light: #ffffff;
    --plum-light: #f6dc93;
    --plum-mid: #eab86a;
    --plum-blush: #d98a5c;
    --plum-shade: #a8794a;
    --blossom-grey: #cfcfcf;
    --amber: #6e4118;
  }
  html, body {
    margin: 0;
    padding: 0;
    width: 857px;
    height: 1200px;
    overflow: hidden;
    background: var(--paper);
  }
  .poster {
    position: relative;
    width: 857px;
    height: 1200px;
    overflow: hidden;
    background: var(--paper);
    font-family: "Noto Serif JP", serif;
  }
  .hero-photo {
    position: absolute;
    inset: 0 0 auto 0;
    height: 800px;
    background:
      radial-gradient(circle at 18% 22%, var(--plum-light) 0 10%, transparent 11%),
      radial-gradient(circle at 62% 12%, var(--plum-mid) 0 8%, transparent 9%),
      radial-gradient(circle at 40% 48%, var(--plum-blush) 0 6%, transparent 7%),
      radial-gradient(circle at 88% 58%, var(--plum-light) 0 9%, transparent 10%),
      radial-gradient(circle at 12% 68%, var(--plum-mid) 0 9%, transparent 10%),
      linear-gradient(165deg, var(--plum-light), var(--plum-mid) 45%, var(--plum-shade) 85%);
    -webkit-mask-image: linear-gradient(to bottom, #000 82%, transparent 100%);
    mask-image: linear-gradient(to bottom, #000 82%, transparent 100%);
  }
  .vertical {
    position: absolute;
    writing-mode: vertical-rl;
    margin: 0;
  }
  .origin-note {
    top: 30px;
    left: 752px;
    font-size: 40px;
    font-weight: 700;
    line-height: 1;
    color: var(--label-light);
    letter-spacing: 0.06em;
  }
  .product-title {
    font-family: "Noto Serif JP", serif;
    font-weight: 700;
    color: var(--title-ink);
    font-size: 150px;
    line-height: 1;
    letter-spacing: 0.02em;
  }
  .title-amber { top: 70px; left: 530px; }
  .title-dew { top: 200px; left: 240px; }
  .abv {
    font-size: 26px;
    line-height: 1;
    font-weight: 500;
    color: var(--label-light);
    border-left: 2px solid var(--label-light);
    padding-left: 6px;
  }
  .abv-amber { top: 420px; left: 455px; }
  .abv-dew { top: 560px; left: 175px; }
  .blossom-branch {
    position: absolute;
    left: 0;
    top: 640px;
    width: 280px;
    height: 560px;
    background: radial-gradient(ellipse at 25% 60%, var(--blossom-grey), rgba(207,207,207,0.2) 55%, transparent 75%);
  }
  .serving {
    position: absolute;
    left: 370px;
    top: 790px;
    width: 380px;
    height: 330px;
    background:
      radial-gradient(circle at 12% 80%, var(--plum-mid) 0 10%, transparent 11%),
      radial-gradient(circle at 90% 78%, var(--plum-light) 0 9%, transparent 10%),
      radial-gradient(ellipse at 45% 50%, var(--amber) 0 30%, rgba(110,65,24,0.2) 42%, transparent 52%);
  }
  .tagline {
    top: 845px;
    left: 585px;
    font-size: 31px;
    line-height: 1.45;
    color: var(--ink);
    font-weight: 500;
  }
  .tagline span { display: block; }
</style>
</head>
<body>
  <main class="poster">
    <div class="hero-photo" role="img" aria-label="木箱に詰められた熟した黄色い南高梅の写真"></div>

    <p class="vertical origin-note">紀州みなべ産南高梅使用</p>

    <h1 class="vertical product-title title-amber">琥珀梅</h1>
    <p class="vertical abv abv-amber">アルコール14%</p>

    <h2 class="vertical product-title title-dew">白露梅</h2>
    <p class="vertical abv abv-dew">アルコール20%</p>

    <div class="blossom-branch" role="img" aria-label="淡い灰色の梅の枝と花の墨絵"></div>
    <div class="serving" role="img" aria-label="氷と梅の実が入った梅酒のグラスと、そばに置かれた青梅"></div>

    <p class="vertical tagline">
      <span>今までにない、</span>
      <span>梅香る甘くない梅酒。</span>
      <span>甘くないので、</span>
      <span>どんな料理にも合う!</span>
    </p>
  </main>
</body>
</html>
```